Label Design - Hair & Beauty Care Wholesaler

Design a label for our client that demonstrates your design skills, your eye for detail and your ability to respond well to the type of brief we produce.

We are offering one prize for the winning design and two participation prizes. The winner will also receive 20 laminated polypropylene labels from the first production run for their portfolio.

Note: This is a test project for us and we know there is a lot of talent out there! Even if you don't win this time, we may be able to engage you for other projects, so if you have the skills and interest we would encourage you to submit a design to make sure we know about you.

One submission only per designer only please.

PROJECT

Our client runs a successful, long-established wholesale hair and beauty care business. Among other things, they sell products like shampoos and conditioners in bulk-buy containers, which hairdressers buy to use in-store in their salons.

(Depending on where you are, the type of product our client needs labels for may be known as a “store brand”, “house brand”, “private label brand”, “own brand”, “home brand” or “generic brand”.)

For this project, the content for the first label to be produced is attached. Keep in mind we will need to be able to change the product name, volume/quantity and ingredients for other labels in future.

Ask questions if you need to! Thanks for participating.

Target Market(s)

Hairdressers and beauty salon owners in Australia.

Industry/Entity Type

Business

Requirements
Must have
• Client's existing logo
All text in the attached "Content" file
Rectangular shape with rounded corners
Finished size 75mm width x 145mm height

```html
<!DOCTYPE html>
<html lang="en">
<head>
<meta charset="utf-8">
<title>Lanolin Shampoo Label</title>
<link rel="stylesheet" href="https://fonts.googleapis.com/css2?family=Source+Sans+3:wght@400;600;700&display=swap">
<style>
  :root {
    --page: #ffffff;
    --red: #d3121f;
    --red-light: #e52a33;
    --red-deep: #a80c17;
    --white: #ffffff;
    --brand-ink: #3a3a1a;
    --shadow: rgba(70, 0, 5, 0.75);
  }
  html, body {
    margin: 0;
    padding: 0;
    width: 996px;
    height: 1200px;
    overflow: hidden;
    background: var(--page);
    font-family: "Source Sans 3", sans-serif;
  }
  .canvas {
    position: relative;
    width: 996px;
    height: 1200px;
  }
  .label {
    position: absolute;
    left: 369px;
    top: 69px;
    width: 496px;
    height: 945px;
    border-radius: 34px;
    overflow: hidden;
    background: radial-gradient(ellipse at 55% 45%, var(--red-light) 0%, var(--red) 55%, var(--red-deep) 100%);
    color: var(--white);
  }
  .label__header {
    position: absolute;
    left: 0;
    top: 0;
    width: 496px;
    height: 200px;
  }
  .label__flourish {
    position: absolute;
    left: -40px;
    top: 430px;
    width: 280px;
    height: 440px;
    border-radius: 50%;
    background: radial-gradient(ellipse at 50% 50%, rgba(150, 8, 18, 0.45) 0%, rgba(150, 8, 18, 0.15) 60%, rgba(150, 8, 18, 0) 100%);
  }
  .brand {
    position: absolute;
    left: 0;
    top: 78px;
    width: 496px;
    text-align: center;
    font-weight: 700;
    font-size: 40px;
    letter-spacing: 3px;
    color: var(--brand-ink);
    text-transform: uppercase;
    line-height: 1;
  }
  .product-name {
    position: absolute;
    left: 0;
    top: 262px;
    width: 496px;
    margin: 0;
    text-align: center;
    font-weight: 700;
    font-size: 72px;
    line-height: 80px;
    text-shadow: 3px 3px 3px var(--shadow);
  }
  .volume {
    position: absolute;
    left: 0;
    top: 470px;
    width: 496px;
    text-align: center;
    font-size: 29px;
    font-weight: 400;
  }
  .ingredients {
    position: absolute;
    left: 70px;
    top: 540px;
    width: 356px;
    text-align: center;
    font-size: 14.5px;
    line-height: 27px;
  }
  .ingredients__title {
    font-weight: 600;
    display: block;
  }
  .supplier {
    position: absolute;
    left: 70px;
    top: 760px;
    width: 356px;
    text-align: center;
    font-size: 14.5px;
    line-height: 24px;
    font-weight: 600;
  }
  .supplier p { margin: 0; }
</style>
</head>
<body>
<div class="canvas">
  <div class="label">
    <svg class="label__header" viewBox="0 0 496 200" aria-hidden="true">
      <defs>
        <linearGradient id="band-shade" x1="0" y1="0" x2="0" y2="1">
          <stop offset="0" stop-color="#ffffff"/>
          <stop offset="1" stop-color="#ececec"/>
        </linearGradient>
      </defs>
      <path d="M0 0 H496 V110 C400 150 250 175 120 165 C70 161 30 150 0 140 Z" fill="url(#band-shade)"/>
      <path d="M0 140 C30 150 70 161 120 165 C250 175 400 150 496 110" fill="none" stroke="#b8b8b8" stroke-width="2" opacity="0.6"/>
    </svg>
    <div class="label__flourish" role="img" aria-label="Faint floral flourish in deep red"></div>

    <div class="brand">Verity</div>

    <h1 class="product-name">Lanolin<br>Shampoo</h1>

    <div class="volume">5 litres</div>

    <div class="ingredients">
      <span class="ingredients__title">Ingredients</span>
      Purified Water, Sodium Laureth Sulphate, Sodium Chloride, Cocamide DEA, Cocamidopropyl Hydroxysultaine, Panthenol, PEG-20 Lanolin, Disodium EDTA, Sodium Hydroxymethyl Glycinate, Citric Acid, Perfume
    </div>

    <div class="supplier">
      <p>Verity Hair and Beauty Supplies</p>
      <p>Unit 8, 42 Harbour Street</p>
      <p>Parramatta NSW 2150</p>
      <p>Telephone (02) 9000 1234 | Fax (02) 9000 5678</p>
      <p>www.verityhairandbeauty.com.au</p>
    </div>
  </div>
</div>
</body>
</html>
```